KAVRO iOS app needs a fun consumer interface design

KAVRO is a file transfer app aimed at consumers to help them get files onto their iOS devices. The app is based around each user having a personalised upload web address, and the ability to issue temporary time limited upload codes to friends and colleagues that they can use to send them files. The first version is already live in the app store but we are working on a second, simplified version. You can see the screen shots for this on www.kavro-example.com and I have attached a quick guide to app flow. The app now looks like a standard templated iOS 7 app. We need a design for the app that give it its own look, whilst retaining the standard iOS cues. It needs to look good on iPhone and iPad. We have a far east techno feel to the app at the moment with our characters, and we want to keep the logo. The website is currently a simple template, there's an ongoing competition to redesign that too - http://jobs.pixelbidhub.example/job.aspx?id=318264
We have a working app with a reasonable design - we are looking for someone to take that design, add the polish a professional designer can bring, to make it pixel perfect and stand out as an app that has great design as well as great functionality.
We are also looking for something that works well on iPhone and iPad. See the attached screenshots of the iPad version - we want that version to look beautiful, not the big empty screen it is now.
Updates
Thanks for the designs so far, they look good. Could you draw them up for iPad size screens too please. The signup/login page and new code pages I think need the most attention as each page doesn't collect that much information, and so a lot of the screen is currently blank. I think we need some sort of background to set the content into for these pages.
The old app is installable for free from the App store if that helps you get a feel for it on the iPad.
Target Market(s)
Consumers, techno savvy
Industry/Entity Type
Store
Font styles to use
Look and feel

```html
<!DOCTYPE html>
<html lang="en">
<head>
<meta charset="utf-8">
<title>KAVRO – New Upload Code</title>
<link rel="stylesheet" href="https://fonts.googleapis.com/css2?family=Open+Sans:wght@300;400;600&display=swap">
<style>
  :root {
    --page: #e9e9e9;
    --panel-top: #ffffff;
    --panel-bottom: #f4f4f4;
    --ink: #4a4a4a;
    --ink-soft: #8a8a8a;
    --ink-faint: #d4d4d4;
    --accent: #2fb0f2;
    --accent-light: #5cc4f7;
    --rule: #e2e2e2;
    --track: #d2d2d2;
  }
  * { box-sizing: border-box; margin: 0; padding: 0; }
  html, body { width: 982px; height: 1200px; overflow: hidden; background: var(--page); }
  body { font-family: "Open Sans", Arial, sans-serif; color: var(--ink); }

  .screen {
    position: relative;
    width: 982px;
    height: 1200px;
    background: var(--panel-bottom);
    overflow: hidden;
  }

  .status-bar {
    position: absolute; top: 0; left: 0; right: 0;
    height: 22px;
    background: #2b2b2b;
    color: #e8e8e8;
    font-size: 13px;
    font-weight: 600;
    display: flex; align-items: center; justify-content: space-between;
    padding: 0 14px;
    z-index: 3;
  }
  .status-bar .carrier { display: flex; align-items: center; gap: 6px; }
  .status-bar .battery { display: flex; align-items: center; gap: 6px; }

  .code-panel {
    position: absolute; top: 22px; left: 0; right: 0;
    height: 363px;
    background: var(--panel-top);
    text-align: center;
    z-index: 2;
  }
  .code-pointer {
    position: absolute; left: 441px; top: 384px;
    z-index: 2;
  }
  .code-title { position: absolute; top: 88px; width: 100%; font-size: 30px; font-weight: 300; color: #5a5a5a; }
  .code-hint { position: absolute; top: 136px; width: 100%; font-size: 22px; font-weight: 300; color: var(--ink-faint); }
  .upload-code {
    position: absolute; top: 182px; width: 100%;
    font-size: 76px; font-weight: 600; letter-spacing: 1px;
    color: var(--accent);
  }

  .share-prompt {
    position: absolute; top: 530px; width: 100%;
    text-align: center; font-size: 30px; font-weight: 300; line-height: 42px; color: var(--ink);
  }
  .email-field {
    position: absolute; top: 676px; left: 188px;
    width: 536px; height: 70px;
    background: #fff;
    display: flex; align-items: center; justify-content: center;
    font-size: 27px; font-weight: 300; color: #6a6a6a;
  }
  .email-field .add-icon { position: absolute; right: 24px; top: 11px; }

  .section-rule {
    position: absolute; top: 857px; left: 94px; width: 794px;
    border-top: 2px solid var(--rule);
  }

  .validity-prompt {
    position: absolute; top: 892px; width: 100%;
    text-align: center; font-size: 30px; font-weight: 300; line-height: 43px; color: var(--ink);
  }
  .validity-slider { position: absolute; top: 1026px; left: 140px; }
  .validity-value {
    position: absolute; top: 1106px; width: 100%;
    text-align: center; font-size: 24px; font-weight: 600; color: var(--ink-soft);
  }
</style>
</head>
<body>
  <main class="screen">
    <div class="status-bar">
      <span class="carrier">
        <svg width="22" height="10" viewBox="0 0 22 10"><rect x="0" y="7" width="3" height="3" fill="#e8e8e8"/><rect x="4.5" y="5" width="3" height="5" fill="#e8e8e8"/><rect x="9" y="3" width="3" height="7" fill="#e8e8e8"/><rect x="13.5" y="1" width="3" height="9" fill="#e8e8e8"/><rect x="18" y="0" width="3" height="10" fill="#e8e8e8"/></svg>
        NOVA
      </span>
      <span class="clock">10:35 AM</span>
      <span class="battery">
        <svg width="11" height="11" viewBox="0 0 11 11"><circle cx="5.5" cy="5.5" r="5" fill="#e8e8e8"/></svg>
        65%
        <svg width="26" height="12" viewBox="0 0 26 12"><rect x="0.5" y="0.5" width="22" height="11" rx="2" fill="none" stroke="#e8e8e8"/><rect x="2" y="2" width="13" height="8" fill="#e8e8e8"/><rect x="23.5" y="3.5" width="2" height="5" fill="#e8e8e8"/></svg>
      </span>
    </div>

    <section class="code-panel">
      <h1 class="code-title">Your new upload code is below</h1>
      <p class="code-hint">Go to kavro-example.com and enter the code</p>
      <p class="upload-code">RX105SWB</p>
    </section>
    <svg class="code-pointer" width="100" height="90" viewBox="0 0 100 90"><polygon points="0,0 100,0 50,90" fill="var(--panel-top)"/></svg>

    <p class="share-prompt">If you want to send the code to someone,<br>enter their email address (optional)</p>
    <div class="email-field">
      test@kavro-example.com
      <svg class="add-icon" width="48" height="48" viewBox="0 0 48 48"><circle cx="24" cy="24" r="21" fill="none" stroke="var(--accent)" stroke-width="2"/><path d="M24 14v20M14 24h20" stroke="var(--accent)" stroke-width="2"/></svg>
    </div>

    <div class="section-rule"></div>

    <p class="validity-prompt">How long should this upload<br>code be valid for?</p>
    <svg class="validity-slider" width="702" height="52" viewBox="0 0 702 52">
      <rect x="0" y="23" width="702" height="6" rx="3" fill="var(--track)"/>
      <rect x="0" y="23" width="312" height="6" rx="3" fill="var(--accent)"/>
      <circle cx="312" cy="26" r="24" fill="var(--accent)"/>
    </svg>
    <p class="validity-value">3 days</p>
  </main>
</body>
</html>
```